Fitness Equipment & Service

I want to make the card eye catching and fun. We are called Corvane Motion Limited and we are based in Wales. We sell, install and service all types of fitness equipment from Skipping ropes, right through the Dumbbells, Kettle bells and Barbells through to state of the art Treadmills, Running Machines and Strength Equipment. We also design and install changing room furniture and lockers.

TYPOGRAPHY
We would like to use Futrura. Futura has an appearance of efficiency and forwardness. The typeface is derived
from simple geometric forms (near-perfect circles, triangles and squares) and is based on strokes of
near-even weight, which are low in contrast. This is most visible in the almost perfectly round stroke of
the o, which is nonetheless slightly ovoid.
The lowercase has tall ascenders, which rise above the cap line. The uppercase
characters present proportions similar to those of classical Roman capitals.

TYPOGRAPHIC CONSIDERATIONS
No Strike though
No Horizontal Scaling
No Drop Shadows
No Effects
Never use less than 120% Leading

OUR CORPORATE COLOURS
BRAND GUIDELINES
We were thinking that our primary colour palette consists of the Acid Green (Pantone 382) and Process Black.

We work closely with tolbrook Ltd and would like to include their name on the card somewhere. I have attached images of the other brands that we work with as an idea or the small icons I have included that illustrate what we do?. I have very kindly been given permission to use any of the images off the files that I have included below, so I hope these help. I will include these below. I would be open to suggestions if it made the card more striking Can you do it?
Updates

Hi All, Just wanted to add a few thoughts but you are the guys with the creative visions (thats why are here) We are based in Wales, UK and we would be open to lots of different ideas on a theme but must be eye catching, Bold and FUN. If you can or think that the Welsh or any dragon could be put in there then go for it (its not a must have) We have also added some ideas for colour but again its over to you!! GO FOR IT ! Thanks and look forward to your visions! Owen

Hi All, Just thought I would sen through the contact details that need to be on the card. (if you want to play around with icons instead of the wording twitter, Facebook, go for it): Corvane Motion Limited Owen Pritchard Managing Director Mob: +44 (0)7382 519 046 e-mail: sales@corvanemotion.co.uk Web: Corvanemotion.co.uk twitter: @motionPostbag Facebook: Corvane Motion Limited

Industry/Entity Type

Fitness

```html
<!DOCTYPE html>
<html lang="en">
<head>
<meta charset="utf-8">
<title>Corvane Motion Limited – Business Card</title>
<link rel="stylesheet" href="https://fonts.googleapis.com/css2?family=Jost:wght@400;500;600;700&display=swap">
<style>
  :root {
    --backdrop: #8c8f90;
    --card: #f3f3f3;
    --navy: #1b2452;
    --gold: #b8923a;
    --ink: #3a3d44;
    --muted: #5c6068;
    --tile-blue: #2b7fc2;
    --tile-sky: #5aa8dc;
    --tile-steel: #1f5d90;
    --tile-slate: #8799a9;
    --tile-night: #1c3a5d;
    --white: #ffffff;
  }
  * { box-sizing: border-box; margin: 0; padding: 0; }
  html, body { width: 1105px; height: 1200px; overflow: hidden; }
  body {
    background: var(--backdrop);
    font-family: "Jost", "Futura", sans-serif;
    position: relative;
  }
  .card {
    position: absolute;
    left: 182px;
    width: 746px;
    height: 427px;
    background: var(--card);
    overflow: hidden;
  }
  .card--front { top: 119px; }
  .card--back { top: 637px; }

  /* Front */
  .brand-mark {
    position: absolute;
    left: 555px; top: 28px;
    width: 120px; height: 120px;
    border-radius: 50%;
    background: var(--navy);
  }
  .brand-name {
    position: absolute;
    right: 33px; top: 168px;
    font-size: 22px; font-weight: 700;
    color: var(--navy);
    line-height: 1.2;
    text-align: right;
  }
  .edge-tab {
    position: absolute;
    left: -16px; top: 226px;
    width: 30px; height: 55px;
    border-radius: 50%;
    background: var(--navy);
  }
  .person { position: absolute; left: 43px; top: 224px; }
  .person__name { font-size: 28px; font-weight: 600; color: var(--navy); line-height: 1.2; }
  .person__role { font-size: 22px; font-weight: 400; color: var(--gold); line-height: 1.3; }
  .divider {
    position: absolute;
    left: 43px; top: 297px;
    width: 670px; height: 2px;
    background: var(--gold);
  }
  .contacts {
    position: absolute;
    left: 43px; top: 317px;
    list-style: none;
  }
  .contacts li {
    display: flex; align-items: center;
    height: 27.5px;
    font-size: 20px; color: var(--ink);
    line-height: 1.2;
  }
  .contacts svg { width: 18px; height: 18px; margin-right: 10px; fill: var(--navy); }
  .address {
    position: absolute;
    right: 33px; top: 343px;
    text-align: right;
    font-size: 20px; color: var(--ink);
    line-height: 1.38;
  }

  /* Back */
  .mosaic {
    position: absolute;
    left: 0; top: 0;
    width: 746px; height: 307px;
    background: linear-gradient(135deg, #1a3556 0%, #0d2340 60%, #132c4a 100%);
    display: grid;
    grid-template-columns: repeat(8, 102px);
    grid-template-rows: repeat(3, 102.3px);
  }
  .tile--blue { background: var(--tile-blue); }
  .tile--sky { background: var(--tile-sky); }
  .tile--steel { background: var(--tile-steel); }
  .tile--slate { background: var(--tile-slate); }
  .tile--night { background: var(--tile-night); }
  .partner {
    position: absolute;
    left: 300px; width: 310px; top: 112px;
    text-align: center;
    color: var(--white);
  }
  .partner__name { font-size: 50px; font-weight: 600; line-height: 1.2; letter-spacing: 1px; }
  .partner__tagline { font-size: 16px; font-weight: 600; line-height: 1.2; letter-spacing: 0.5px; }
  .social {
    position: absolute;
    left: 0; width: 746px; top: 333px;
    text-align: center;
    font-size: 26px; line-height: 1.27;
    color: var(--muted);
  }
  .social__label { color: #1e1f22; }
</style>
</head>
<body>

  <section class="card card--front">
    <div class="brand-mark"></div>
    <div class="brand-name">Corvane Motion Limited</div>
    <div class="edge-tab"></div>

    <div class="person">
      <div class="person__name">Owen Pritchard</div>
      <div class="person__role">Managing Director</div>
    </div>
    <div class="divider"></div>

    <ul class="contacts">
      <li>
        <svg viewBox="0 0 18 18" aria-hidden="true"><path d="M5 1h8a1.5 1.5 0 0 1 1.5 1.5v13A1.5 1.5 0 0 1 13 17H5a1.5 1.5 0 0 1-1.5-1.5v-13A1.5 1.5 0 0 1 5 1zm0 2v11h8V3z"/></svg>
        +44 (0)7382 519 046
      </li>
      <li>
        <svg viewBox="0 0 18 18" aria-hidden="true"><path d="M1 4h16v10H1zM2.5 5.5 9 10l6.5-4.5v-.2L9 9.3 2.5 5.3z"/></svg>
        sales@corvanemotion.co.uk
      </li>
      <li>
        <svg viewBox="0 0 18 18" aria-hidden="true"><circle cx="9" cy="9" r="8"/><path d="M5 6c2 0 3 1 3 2.5S6 10 6 12l-2-1c0-2 1-2.5 1-5zM11 4c2 1 3 3 2 5-1-1-3 0-3-2s1-2 1-3z" fill="#f3f3f3"/></svg>
        www.Corvanemotion.co.uk
      </li>
    </ul>

    <div class="address">4120 Larkfield Road<br>Bramwell, Alaska 34817</div>
  </section>

  <section class="card card--back">
    <div class="mosaic" role="img" aria-label="Gym interior photo overlaid with tiles of fitness service icons">
      <span class="tile--blue"></span><span class="tile--sky"></span><span></span><span></span><span class="tile--blue"></span><span class="tile--steel"></span><span></span><span class="tile--slate"></span>
      <span></span><span class="tile--slate"></span><span class="tile--blue"></span><span></span><span></span><span></span><span class="tile--night"></span><span class="tile--blue"></span>
      <span></span><span></span><span class="tile--steel"></span><span></span><span class="tile--sky"></span><span class="tile--slate"></span><span></span><span class="tile--blue"></span>
    </div>
    <div class="partner">
      <div class="partner__name">TOLBROOK</div>
      <div class="partner__tagline">KEEPING GYMS RUNNING</div>
    </div>
    <div class="social">
      <div><span class="social__label">Twitter:</span> @motionPostbag</div>
      <div><span class="social__label">Facebook:</span> Corvane Motion Limited</div>
    </div>
  </section>

</body>
</html>
```